WEB Portal and mobile app design is needed

Now we are making a WEB portal nad mobile apps for patient of clinics. One of functions of portal and app is connecting with medical devices like this http://www.vornacare.example/ . So we need a design of user interface for vizualization of mesuring blood presure and hert rate, glucose level, blood oxygenation level, weight and other. Design must be simple and friendly for user. Also this interface must show normal and abnormal level of evry parameter.
Industry/Entity Type
Graphic Design

```html
<!DOCTYPE html>
<html lang="en">
<head>
<meta charset="utf-8">
<title>Vital Signs App Screens</title>
<link rel="stylesheet" href="https://fonts.googleapis.com/css2?family=Open+Sans:wght@400;600;700&family=PT+Sans+Narrow:wght@400;700&display=swap">
<style>
:root{
  --page:#ffffff;
  --status:#111111;
  --screen-bg:#dfe9f5;
  --card:#ffffff;
  --ink:#222222;
  --muted:#555555;
  --rule:#e2e2e2;
  --oxygen:#8fcf1f;
  --pressure:#ef3d3d;
  --glucose:#1ca6e3;
  --healthy:#8ccc1c;
  --notes:#1a8fcb;
  --nav-bg:#f4f4f4;
  --nav-ink:#666666;
  --g1:#a9cf5a;
  --g2:#d9e07a;
  --g3:#f6cf5c;
  --g4:#f6a13f;
  --g5:#ee7a2e;
}
*{box-sizing:border-box;margin:0;padding:0}
html,body{width:1200px;height:729px;overflow:hidden;background:var(--page)}
body{position:relative;font-family:"Open Sans",Arial,sans-serif;color:var(--ink)}
.screen{position:absolute;width:305px;height:457px;background:var(--screen-bg);overflow:hidden}
.screen--oxygen{left:64px;top:133px}
.screen--pressure{left:472px;top:138px}
.screen--glucose{left:862px;top:140px}
.status-bar{height:17px;background:var(--status);color:#fff;font-size:11px;font-weight:600;display:flex;align-items:center;justify-content:space-between;padding:0 8px}
.status-bar .signal{display:flex;align-items:flex-end;gap:1px}
.status-bar .signal i{display:block;width:2px;background:#fff}
.status-bar .battery{width:18px;height:8px;border:1px solid #fff;padding:1px}
.status-bar .battery span{display:block;height:100%;background:#fff}
.card{position:absolute;left:28px;top:48px;width:250px;height:330px;background:var(--card)}
.card-header{height:34px;display:flex;align-items:center;justify-content:space-between;padding:0 6px;color:#fff;font-weight:700;font-size:14px;letter-spacing:.2px}
.screen--oxygen .card-header{background:var(--oxygen)}
.screen--pressure .card-header{background:var(--pressure)}
.screen--glucose .card-header{background:var(--glucose)}
.arrow-btn{width:24px;height:24px;background:#fff;border-radius:3px;display:flex;align-items:center;justify-content:center}
.date{text-align:center;font-size:13px;padding:14px 0 6px}
.metrics{height:120px;display:flex;margin:0 2px}
.metric{flex:1;display:flex;flex-direction:column;align-items:center;justify-content:center}
.metric + .metric{border-left:1px solid var(--rule)}
.big{font-family:"PT Sans Narrow",Arial,sans-serif;font-size:72px;line-height:.9;color:var(--ink)}
.big small{font-size:44px}
.label{font-size:14px;color:var(--ink)}
.pressure-table{display:grid;grid-template-columns:1fr 1fr .8fr;margin:4px 4px 0;height:116px}
.pressure-table .cell{display:flex;flex-direction:column;align-items:center;justify-content:center;border-right:1px solid var(--rule)}
.pressure-table .cell:nth-child(3n){border-right:none}
.pressure-table .head{border-bottom:1px solid var(--rule);height:52px;position:relative}
.head strong{font-size:16px;font-weight:700;line-height:1.1}
.head span{font-size:8px;color:var(--muted)}
.head .heart{position:absolute;top:2px}
.pressure-table .value{font-family:"PT Sans Narrow",Arial,sans-serif;font-size:42px}
.glucose-info{display:flex;flex-direction:column;justify-content:center;gap:14px;padding-left:6px}
.glucose-row{display:flex;align-items:center;gap:8px;font-size:14px;line-height:1.25}
.glucose-row .thumb{width:44px;height:40px;border-radius:4px}
.thumb--pill{background:linear-gradient(135deg,#d92b2b 0 50%,#e9eef2 50%)}
.thumb--meal{background:linear-gradient(180deg,#d98b2e,#6b8f2a 55%,#b5562b)}
.gauge{position:absolute;left:10px;top:200px;width:230px;height:120px}
.gauge-text{position:absolute;left:0;right:0;top:255px;text-align:center}
.gauge-text .state{font-size:9px;display:block}
.gauge-text .reading{font-family:"PT Sans Narrow",Arial,sans-serif;font-size:62px;line-height:.95;color:var(--healthy)}
.notes{position:absolute;left:28px;top:383px;width:250px;height:26px;background:#f6f6f6;border:1px solid #d8d8d8;display:flex;justify-content:flex-end}
.notes span{background:var(--notes);color:#fff;font-size:13px;width:66px;display:flex;align-items:center;justify-content:center}
.nav{position:absolute;left:0;bottom:0;width:305px;height:43px;background:var(--nav-bg);display:flex;border-top:1px solid #d6d6d6}
.nav-item{flex:1;display:flex;align-items:center;justify-content:center;gap:3px;font-size:11px;color:var(--nav-ink);border-right:1px solid #d6d6d6}
.nav-item:last-child{border-right:none}
</style>
</head>
<body>

<svg width="0" height="0" style="position:absolute" aria-hidden="true">
  <defs>
    <linearGradient id="gauge-fill" x1="0" x2="1" y1="0" y2="0">
      <stop offset="0" stop-color="var(--g1)"/>
      <stop offset=".3" stop-color="var(--g2)"/>
      <stop offset=".5" stop-color="var(--g3)"/>
      <stop offset=".75" stop-color="var(--g4)"/>
      <stop offset="1" stop-color="var(--g5)"/>
    </linearGradient>
    <symbol id="gauge-dial" viewBox="0 0 230 120">
      <path d="M3 115 A112 112 0 0 1 227 115" fill="none" stroke="#e8e8e8" stroke-width="3"/>
      <path d="M15 115 A100 100 0 0 1 215 115" fill="none" stroke="url(#gauge-fill)" stroke-width="24"/>
      <g stroke="#fff" stroke-width="2" opacity=".7">
        <line x1="30" y1="92.2" x2="6.8" y2="86"/><line x1="38.8" y1="71" x2="18" y2="59"/>
        <line x1="52.8" y1="52.8" x2="35.8" y2="35.8"/><line x1="71" y1="38.8" x2="59" y2="18"/>
        <line x1="92.2" y1="30" x2="86" y2="6.8"/><line x1="115" y1="27" x2="115" y2="3"/>
        <line x1="137.8" y1="30" x2="144" y2="6.8"/><line x1="159" y1="38.8" x2="171" y2="18"/>
        <line x1="177.2" y1="52.8" x2="194.2" y2="35.8"/><line x1="191.2" y1="71" x2="212" y2="59"/>
        <line x1="200" y1="92.2" x2="223.2" y2="86"/>
      </g>
      <path d="M119 34 L131 38 L123 44 Z" fill="#fff" stroke="#bbb" stroke-width=".8"/>
    </symbol>
    <symbol id="icon-home" viewBox="0 0 20 20"><path d="M2 10 L10 3 L18 10 M4 9 V18 H16 V9" fill="none" stroke="#777" stroke-width="1.3"/></symbol>
    <symbol id="icon-delete" viewBox="0 0 20 20"><circle cx="10" cy="10" r="8" fill="none" stroke="#777" stroke-width="1.3"/><path d="M6.5 6.5 L13.5 13.5 M13.5 6.5 L6.5 13.5" stroke="#777" stroke-width="1.3"/></symbol>
    <symbol id="icon-again" viewBox="0 0 20 20"><path d="M4 8 A7 7 0 1 1 5 15" fill="none" stroke="#777" stroke-width="1.3"/><path d="M1 6 L4 9 L7 6" fill="none" stroke="#777" stroke-width="1.3"/></symbol>
    <symbol id="icon-history" viewBox="0 0 20 20"><path d="M4 2 H13 L17 6 V19 H4 Z" fill="none" stroke="#777" stroke-width="1.3"/><path d="M7 9 H14 M7 12 H14 M7 15 H14" stroke="#777" stroke-width="1.2"/></symbol>
  </defs>
</svg>

<!-- Oxygen level -->
<section class="screen screen--oxygen">
  <div class="status-bar"><span class="signal"><i style="height:3px"></i><i style="height:5px"></i><i style="height:7px"></i><i style="height:9px"></i>&nbsp;3G</span><span>4:20 PM</span><span class="battery"><span></span></span></div>
  <div class="card">
    <div class="card-header">
      <span class="arrow-btn"><svg width="10" height="12"><path d="M9 1 L1 6 L9 11Z" fill="var(--oxygen)"/></svg></span>
      <span>OXYGEN LEVEL</span>
      <span class="arrow-btn"><svg width="10" height="12"><path d="M1 1 L9 6 L1 11Z" fill="var(--oxygen)"/></svg></span>
    </div>
    <p class="date">April 22, 2014 4:30 PM</p>
    <div class="metrics">
      <div class="metric"><span class="big">98<small>%</small></span><span class="label" style="font-size:13px">SPO2</span></div>
      <div class="metric"><span class="big">101</span><span class="label">Heart Rate</span></div>
    </div>
    <svg class="gauge"><use href="#gauge-dial"/></svg>
    <div class="gauge-text"><span class="state">Healty</span><span class="reading">101</span></div>
  </div>
  <div class="notes"><span>Notes</span></div>
  <nav class="nav">
    <span class="nav-item"><svg width="20" height="20"><use href="#icon-home"/></svg>HOME</span>
    <span class="nav-item"><svg width="20" height="20"><use href="#icon-delete"/></svg>DELETE</span>
    <span class="nav-item"><svg width="20" height="20"><use href="#icon-again"/></svg>AGAIN</span>
    <span class="nav-item"><svg width="20" height="20"><use href="#icon-history"/></svg>HISTORY</span>
  </nav>
</section>

<!-- Blood pressure -->
<section class="screen screen--pressure">
  <div class="status-bar"><span class="signal"><i style="height:3px"></i><i style="height:5px"></i><i style="height:7px"></i><i style="height:9px"></i>&nbsp;3G</span><span>4:20 PM</span><span class="battery"><span></span></span></div>
  <div class="card">
    <div class="card-header">
      <span class="arrow-btn"><svg width="10" height="12"><path d="M9 1 L1 6 L9 11Z" fill="var(--pressure)"/></svg></span>
      <span>BLOOD PRESSURE</span>
      <span class="arrow-btn"><svg width="10" height="12"><path d="M1 1 L9 6 L1 11Z" fill="var(--pressure)"/></svg></span>
    </div>
    <p class="date">April 22, 2014 4:30 PM</p>
    <div class="pressure-table">
      <div class="cell head"><svg class="heart" width="12" height="11" viewBox="0 0 12 11"><path d="M6 10.5 L1 5.5 A2.8 2.8 0 0 1 6 2 A2.8 2.8 0 0 1 11 5.5 Z" fill="var(--pressure)"/></svg><strong style="margin-top:8px">PULSE</strong><span>Beats / min</span></div>
      <div class="cell head"><strong style="font-size:19px">SYS</strong><span>mmHg</span></div>
      <div class="cell head"><strong style="font-size:19px">DIA</strong><span>mmHg</span></div>
      <div class="cell value">72</div>
      <div class="cell value">128</div>
      <div class="cell value">69</div>
    </div>
    <svg class="gauge"><use href="#gauge-dial"/></svg>
    <div class="gauge-text"><span class="state">Healty</span><span class="reading">128</span></div>
  </div>
  <div class="notes"><span>Notes</span></div>
  <nav class="nav">
    <span class="nav-item"><svg width="20" height="20"><use href="#icon-home"/></svg>HOME</span>
    <span class="nav-item"><svg width="20" height="20"><use href="#icon-delete"/></svg>DELETE</span>
    <span class="nav-item"><svg width="20" height="20"><use href="#icon-again"/></svg>AGAIN</span>
    <span class="nav-item"><svg width="20" height="20"><use href="#icon-history"/></svg>HISTORY</span>
  </nav>
</section>

<!-- Glucose level -->
<section class="screen screen--glucose">
  <div class="status-bar"><span class="signal"><i style="height:3px"></i><i style="height:5px"></i><i style="height:7px"></i><i style="height:9px"></i>&nbsp;3G</span><span>4:20 PM</span><span class="battery"><span></span></span></div>
  <div class="card">
    <div class="card-header">
      <span class="arrow-btn"><svg width="10" height="12"><path d="M9 1 L1 6 L9 11Z" fill="var(--glucose)"/></svg></span>
      <span>GLUCOSE LEVEL</span>
      <span class="arrow-btn"><svg width="10" height="12"><path d="M1 1 L9 6 L1 11Z" fill="var(--glucose)"/></svg></span>
    </div>
    <p class="date">April 22, 2014 4:30 PM</p>
    <div class="metrics">
      <div class="metric glucose-info" style="align-items:flex-start">
        <div class="glucose-row"><span class="thumb thumb--pill" role="img" aria-label="Medicine capsule illustration"></span><span>Pre<br>Medicine</span></div>
        <div class="glucose-row"><span class="thumb thumb--meal" role="img" aria-label="Burger illustration for lunch"></span><span>Post<br>Lunch</span></div>
      </div>
      <div class="metric"><span class="big">108</span><span class="label">mg/dL</span></div>
    </div>
    <svg class="gauge"><use href="#gauge-dial"/></svg>
    <div class="gauge-text"><span class="state">Healty</span><span class="reading">108</span></div>
  </div>
  <div class="notes"><span>Notes</span></div>
  <nav class="nav">
    <span class="nav-item"><svg width="20" height="20"><use href="#icon-home"/></svg>HOME</span>
    <span class="nav-item"><svg width="20" height="20"><use href="#icon-delete"/></svg>DELETE</span>
    <span class="nav-item"><svg width="20" height="20"><use href="#icon-again"/></svg>AGAIN</span>
    <span class="nav-item"><svg width="20" height="20"><use href="#icon-history"/></svg>HISTORY</span>
  </nav>
</section>

</body>
</html>
```